brindlewood carpentry business card 2.0

id like to get some extra info added to my current business card ,but i am also open to a new design as well ,id like it to be a clean professional look
i have attached the original card files, i have also attached the ridgemark guild logo and licensed builder logo that id like to add to all the current info on the old card
also the color green is important as seen in the company logo

Industry/Entity Type

Carpentry

Colors
9bcb3c

```html
<!DOCTYPE html>
<html lang="en">
<head>
<meta charset="utf-8">
<title>Brindlewood Carpentry — Business Card</title>
<link rel="stylesheet" href="https://fonts.googleapis.com/css2?family=Montserrat:wght@500;600;700&display=swap">
<style>
  :root {
    --backdrop: #2b2b2b;
    --card: #ffffff;
    --ink: #111111;
    --green: #9bcb3c;
    --orange: #f29a1f;
    --badge-navy: #1f3f8f;
    --badge-gold: #f6c21c;
    --badge-grey: #6b6b6b;
  }
  * { box-sizing: border-box; margin: 0; padding: 0; }
  html, body { width: 1200px; height: 900px; overflow: hidden; }
  body {
    background: var(--backdrop);
    font-family: "Montserrat", sans-serif;
    position: relative;
  }
  .card {
    position: absolute;
    width: 640px;
    height: 390px;
    background: var(--card);
    border-radius: 26px;
    overflow: hidden;
  }
  .card--front { left: 90px; top: 50px; }
  .card--back  { left: 470px; top: 465px; }

  .holder { position: absolute; left: 52px; top: 150px; }
  .holder__name {
    font-weight: 700; font-size: 21px; color: var(--ink); letter-spacing: 0.5px;
  }
  .holder__role {
    font-weight: 500; font-size: 15px; color: var(--green); margin-top: 2px;
  }
  .holder__rule {
    width: 22px; height: 3px; background: var(--ink); margin-top: 10px;
  }

  .brand { position: absolute; right: 46px; top: 72px; text-align: right; }
  .brand__name {
    display: flex; align-items: center; justify-content: flex-end; gap: 10px;
    font-weight: 600; font-size: 34px; color: var(--ink); letter-spacing: 2px;
  }
  .brand__mark { width: 12px; height: 12px; background: var(--green); }
  .brand__sub {
    font-weight: 600; font-size: 34px; color: var(--ink); letter-spacing: 2px;
    line-height: 1.1;
  }

  .badges {
    position: absolute; right: 46px; top: 190px;
    display: flex; gap: 14px; align-items: center;
  }
  .badge--guild { width: 58px; height: 58px; background: var(--badge-navy); }
  .badge--licence {
    width: 62px; height: 62px; border-radius: 50%;
    border: 3px solid var(--badge-grey); background: #e9e9e9;
  }

  .contacts {
    position: absolute; left: 52px; bottom: 40px;
    list-style: none; display: grid; gap: 10px;
  }
  .contacts__item {
    display: flex; align-items: center; gap: 12px;
    font-weight: 500; font-size: 15px; color: var(--ink);
  }
  .contacts__icon { width: 16px; height: 16px; flex: none; }

  .pattern-fill {
    position: absolute; inset: 0;
    background: linear-gradient(135deg, #ffffff 0%, #eef6dc 45%, #ffffff 60%, #e6f1cc 100%);
  }
</style>
</head>
<body>

<section class="card card--front">
  <div class="holder">
    <p class="holder__name">MARCUS HALE</p>
    <p class="holder__role">Director Brindlewood Carpentry Ltd</p>
    <div class="holder__rule"></div>
  </div>

  <div class="brand">
    <p class="brand__name"><span class="brand__mark"></span>BRINDLEWOOD</p>
    <p class="brand__sub">CARPENTRY</p>
  </div>

  <div class="badges">
    <div class="badge--guild" aria-label="Ridgemark Guild member badge"></div>
    <div class="badge--licence" aria-label="Licensed builder badge"></div>
  </div>

  <ul class="contacts">
    <li class="contacts__item">
      <svg class="contacts__icon" viewBox="0 0 16 16"><path d="M3 1l3 3-1.5 2a8 8 0 0 0 5.5 5.5L12 10l3 3-2 2C6 15 1 10 1 3z" fill="var(--green)"/></svg>
      021 048 365 90
    </li>
    <li class="contacts__item">
      <svg class="contacts__icon" viewBox="0 0 16 16"><rect x="1" y="3" width="14" height="10" fill="var(--orange)"/><path d="M1 3l7 6 7-6" stroke="#fff" stroke-width="1.4" fill="none"/></svg>
      marcus@brindlewoodcarpentry.co.nz
    </li>
    <li class="contacts__item">
      <svg class="contacts__icon" viewBox="0 0 16 16" fill="none" stroke="var(--green)" stroke-width="1.4"><circle cx="8" cy="8" r="6.5"/><ellipse cx="8" cy="8" rx="3" ry="6.5"/><path d="M1.5 8h13M3 4.5h10M3 11.5h10"/></svg>
      www.brindlewoodcarpentry.co.nz
    </li>
  </ul>
</section>

<section class="card card--back">
  <div class="pattern-fill" role="img" aria-label="Repeating brand name pattern in black and green across the card back"></div>
</section>

</body>
</html>
```